Pellory Wealth Management - website refresh

www.pellorywealth-example.com. We are a UK wealth management company. The website is looking tired and old.
We would like to keep similar content ie works and overall structure, just improve the look of the website and modernise the site. Needs to be a professional financial site.
Looking for suggestions for new photos and graphics.
would like to keep plugins for the poll otter links and market lens widgets that are currently embedded.
would like to keep "our process" graphic.
"portfolio advisory service" page can go, as no longer applicable.
the "client log in" tab can link to this, our new back office system https://pellorywm.gb.vxq-example.net/
Would like colours that work with logo
like images and styles of these sites, same target market
https://www.tindalforsyth-example.com/
https://www.makrel-example.co.uk/
Examples of other wealth managers/IFA's in out industry that we like
https://www.solvirowealth-example.co.uk/
www.lanternQX-example.com
https://orbent-uk-example.com/
https://quentinharrow-example.com/
https://www.velmorwealthplanning-example.co.uk/here-for-you/
https://zrkwealth-example.co.uk/
http://www.dunvix-example.org/
https://www.fenwarrowwealth-example.co.uk/
http://www.unitedcircleofautonomousplanners-example.com/global-membership/
http://www.torquilwealth-example.co.uk/
https://www.keystrelbaxter-example.co.uk/our-values
https://qjtw-example.co.uk/
Target Market(s)
retail customers, professionals.
Industry/Entity Type
uk wealth management
Coding
Coded - Design and coding required
Number of Pages Required
5+ page
Look and feel
Each slider illustrates characteristics of the customer's brand and the style your logo design should communicate.

```html
<!DOCTYPE html>
<html lang="en">
<head>
<meta charset="utf-8">
<title>Pellory Wealth Management</title>
<link href="https://fonts.googleapis.com/css2?family=DM+Sans:wght@400;500;700&family=Playfair+Display:wght@600;700&display=swap" rel="stylesheet">
<style>
:root{
  --navy:#0f1f4b;
  --navy-deep:#0c1a40;
  --teal:#2b7f78;
  --teal-light:#3a938b;
  --ice:#eef5f8;
  --ink:#1b2340;
  --muted:#6b7385;
  --white:#ffffff;
  --serif:'Playfair Display', Georgia, serif;
  --sans:'DM Sans', Arial, sans-serif;
}
*{box-sizing:border-box;margin:0;padding:0}
html,body{width:1200px;height:4573px;overflow:hidden}
body{position:relative;font-family:var(--sans);color:var(--ink);background:var(--white)}
.abs{position:absolute}
.photo{position:absolute}
a{color:inherit;text-decoration:none}

/* hero */
.hero{position:absolute;left:0;top:0;width:1200px;height:865px;overflow:hidden}
.hero .photo{inset:0;background:linear-gradient(120deg,#6f7b86 0%,#b9b4ad 45%,#7d7067 70%,#3c3f4a 100%)}
.hero svg.shapes{position:absolute;inset:0}
.nav{position:absolute;left:112px;top:18px;width:973px;height:85px;background:var(--white);display:flex;align-items:center;box-shadow:0 4px 18px rgba(0,0,0,.12)}
.brand{display:flex;align-items:center;gap:10px;padding-left:14px;width:225px}
.brand-dot{width:30px;height:30px;border-radius:50%;background:var(--teal)}
.brand-name{font-family:var(--sans);font-weight:700;font-size:16px;color:var(--navy);letter-spacing:.5px}
.menu{display:flex;gap:26px;font-size:15px;color:var(--ink);margin-left:30px}
.menu .active{color:var(--teal);font-weight:700}
.call{position:absolute;right:0;top:0;width:215px;height:85px;background:var(--teal);color:var(--white);display:flex;align-items:center;gap:12px;padding-left:22px}
.call small{display:block;font-size:12px;opacity:.9}
.call b{font-size:18px;font-weight:500}
.hero h1{position:absolute;left:103px;top:252px;width:640px;font-family:var(--serif);font-weight:700;font-size:72px;line-height:77px;color:var(--white)}
.hero p{position:absolute;left:103px;top:498px;width:520px;font-size:17px;line-height:28px;color:var(--white)}
.btn{position:absolute;background:var(--teal);color:var(--white);font-size:15px;display:flex;align-items:center;justify-content:center}

/* about */
.stat-box{position:absolute;color:var(--white);text-align:center;display:flex;flex-direction:column;justify-content:center}
.stat-box b{font-weight:400;font-size:30px}
.stat-box span{font-size:15px;margin-top:6px}
.eyebrow{font-size:13px;letter-spacing:1.5px;color:var(--teal);text-transform:uppercase}
.h2{font-family:var(--serif);font-weight:700;color:var(--navy)}
.body-text{font-size:15px;line-height:24px;color:var(--muted)}
.feature{position:absolute;left:726px;display:flex;gap:18px;width:380px}
.feature h4{font-family:var(--serif);font-size:18px;color:var(--teal);margin-bottom:6px}

/* services */
.services{position:absolute;left:0;top:1642px;width:1200px;height:756px;background:var(--ice)}
.card{position:absolute;top:208px;width:307px;height:442px;background:var(--white);text-align:center}
.card .photo{left:0;top:0;width:307px;height:215px}
.card .icon{position:absolute;left:116px;top:180px;width:76px;height:71px;background:var(--teal);display:flex;align-items:center;justify-content:center}
.card h3{position:absolute;top:287px;width:100%;font-family:var(--serif);font-size:19px;color:var(--navy)}
.card p{position:absolute;top:322px;left:34px;width:239px;font-size:14.5px;line-height:24px;color:var(--muted)}
.card .go{position:absolute;top:406px;left:145px}

/* mission */
.mission{position:absolute;left:0;top:2398px;width:1200px;height:650px;background:var(--navy)}
.mission .photo{left:0;top:0;width:600px;height:570px;background:linear-gradient(135deg,#6d6154 0%,#a89883 50%,#d7d2cc 100%)}
.mission .copy{position:absolute;left:667px;top:0;width:330px;height:570px;overflow:hidden;color:var(--white)}
.mission h2{font-family:var(--serif);font-size:42px;line-height:44px;margin-top:54px}
.mission p{font-size:15px;line-height:24px;margin-top:22px}
.mission .sig{font-family:var(--serif);font-size:19px;margin-top:24px}
.counter{position:absolute;top:2968px;width:225px;height:183px;background:var(--teal);color:var(--white);text-align:center;padding-top:28px}
.counter b{display:block;font-size:30px;font-weight:400;margin-top:14px}
.counter span{font-size:15px}
.counter::after{content:"";position:absolute;right:0;bottom:0;border-style:solid;border-width:0 0 14px 14px;border-color:transparent transparent var(--white) transparent}

/* cases */
.case{position:absolute;width:474px;height:348px;overflow:hidden}
.case .photo{inset:0}
.case .shade{position:absolute;inset:0;background:linear-gradient(180deg,rgba(15,31,75,0) 40%,rgba(15,31,75,.55) 100%)}
.case small{position:absolute;left:30px;top:228px;font-size:14px;color:var(--white)}
.case h3{position:absolute;left:27px;top:252px;font-family:var(--serif);font-size:20px;color:var(--white)}
.case .go{position:absolute;left:30px;top:297px;width:36px;height:34px;background:rgba(255,255,255,.25);display:flex;align-items:center;justify-content:center}

/* footer */
.footer{position:absolute;left:0;top:4235px;width:1200px;height:338px;background:var(--navy);color:var(--white)}
.footer .panel{position:absolute;left:99px;top:0;width:270px;height:288px;background:var(--teal);padding:40px 0 0 42px}
.footer .panel .brand{padding-left:0;width:auto}
.footer .panel .brand-dot{background:var(--white)}
.footer .panel .brand-name{color:var(--white)}
.contact{font-size:13.5px;margin-top:16px;display:flex;gap:12px;align-items:flex-start;line-height:17px}
.col{position:absolute;top:50px}
.col h4{font-family:var(--serif);font-size:19px;margin-bottom:18px}
.col li{list-style:none;font-size:13.5px;line-height:27.5px;opacity:.92}
.email{width:214px;height:48px;background:var(--white);display:flex;align-items:center;justify-content:space-between;padding-left:18px;font-size:13px;color:var(--ink);border:1px solid #d6dbe6}
.email i{width:48px;height:40px;margin-right:4px;background:var(--teal);display:flex;align-items:center;justify-content:center}
.social{display:flex;gap:20px;margin-top:14px;padding-left:10px}
.social span{width:8px;height:8px;border-radius:50%;background:var(--white)}
.copyright{position:absolute;left:0;bottom:16px;width:100%;text-align:center;font-size:12px;opacity:.8}
</style>
</head>
<body>

<section class="hero">
  <div class="photo" role="img" aria-label="Photo of smiling colleagues reviewing documents together"></div>
  <svg class="shapes" width="1200" height="865" viewBox="0 0 1200 865">
    <polygon points="0,0 460,0 852,865 0,865" fill="#0f1f4b" opacity=".96"/>
    <polygon points="1200,515 1200,865 754,865" fill="#2b7f78"/>
  </svg>
  <nav class="nav">
    <div class="brand"><span class="brand-dot"></span><span class="brand-name">PELLORY</span></div>
    <div class="menu"><a class="active">Home</a><a>About us</a><a>Services</a><a>Cases</a><a>Contact us</a><a>More &#8964;</a></div>
    <div class="call">
      <svg width="26" height="26" viewBox="0 0 24 24" fill="none" stroke="#fff" stroke-width="1.4"><path d="M5 3h4l2 5-3 2a11 11 0 0 0 6 6l2-3 5 2v4a2 2 0 0 1-2 2A17 17 0 0 1 3 5a2 2 0 0 1 2-2z"/></svg>
      <div><small>Call us at:</small><b>+44 20 7946 0182</b></div>
    </div>
  </nav>
  <h1>Our Finance Can Give Possibilities For Business</h1>
  <p>Duis aute irure dolor in reprehenderit in voluptate velit cillum dolore eu fugiat nulla pariatur.</p>
  <a class="btn" style="left:103px;top:588px;width:193px;height:56px">Discover More</a>
</section>

<section class="about">
  <svg class="abs" style="left:0;top:960px" width="110" height="160" viewBox="0 0 110 160">
    <rect x="53" y="16" width="28" height="28" transform="rotate(45 67 30)" fill="#2b7f78"/>
    <rect x="-3" y="32" width="98" height="98" transform="rotate(45 46 82)" fill="#0f1f4b"/>
  </svg>
  <div class="abs" style="left:101px;top:1212px;width:2px;height:318px;background:var(--teal)"></div>
  <div class="abs" style="left:101px;top:1528px;width:121px;height:2px;background:var(--teal)"></div>
  <div class="photo" style="left:124px;top:1079px;width:201px;height:426px;background:linear-gradient(160deg,#9a9187,#d9d3cb 60%,#c5c6c9)" role="img" aria-label="Photo of colleagues discussing paperwork"></div>
  <div class="photo" style="left:337px;top:971px;width:334px;height:429px;background:linear-gradient(180deg,#dfe2e4,#c2c6cb 50%,#2c3345)" role="img" aria-label="Photo of a smiling businessman in a suit"></div>
  <div class="stat-box" style="left:160px;top:973px;width:165px;height:119px;background:var(--teal)"><b>850+</b><span>Awards</span></div>
  <div class="stat-box" style="left:474px;top:1393px;width:184px;height:112px;background:var(--navy)"><b>1,500+</b><span>Projects</span></div>
  <svg class="abs" style="left:644px;top:1491px" width="14" height="14"><polygon points="14,0 14,14 0,14" fill="#fff"/></svg>

  <div class="eyebrow abs" style="left:726px;top:992px">About us</div>
  <h2 class="h2 abs" style="left:726px;top:1016px;font-size:42px;line-height:46px;width:420px">Get Exceptional Service For Growth</h2>
  <p class="body-text abs" style="left:726px;top:1120px;width:380px">Quis autem vel eum iure reprehenderit aui in eavoua ate velit esse quam nihil molestiae consequatur ver illum aui dolorem eum fugiat.</p>
  <div class="feature" style="top:1217px">
    <svg width="46" height="46" viewBox="0 0 46 46" fill="none" stroke="#2b7f78" stroke-width="2"><circle cx="20" cy="26" r="16"/><circle cx="20" cy="26" r="10"/><circle cx="20" cy="26" r="4"/><path d="M20 26 40 6M34 6h6v6"/></svg>
    <div><h4>Our Mission</h4><p class="body-text" style="font-size:14.5px">Duam nihil molestiae consequatur ver illu aui dolorem eum fugiat.</p></div>
  </div>
  <div class="feature" style="top:1310px">
    <svg width="46" height="46" viewBox="0 0 46 46" fill="none" stroke="#2b7f78" stroke-width="2"><path d="M4 42 20 14l8 12 5-6 9 22z"/><path d="M20 14V4h10l-3 3 3 3H20"/></svg>
    <div><h4>Our Goals</h4><p class="body-text" style="font-size:14.5px">Reprehenderit aui in ea voluptate velit ess nihil molestiae vel illum.</p></div>
  </div>
  <a class="btn" style="left:726px;top:1416px;width:218px;height:57px">Read More</a>
</section>

<section class="services">
  <div class="eyebrow abs" style="left:0;width:1200px;text-align:center;top:102px">Our services</div>
  <h2 class="h2 abs" style="left:0;width:1200px;text-align:center;top:124px;font-size:40px">What We’re Offering</h2>

  <article class="card" style="left:112px">
    <div class="photo" style="background:linear-gradient(135deg,#4a4f58,#a9b3bf 60%,#e7ecf1)" role="img" aria-label="Photo of coins and a financial chart on a desk"></div>
    <div class="icon"><svg width="34" height="34" viewBox="0 0 34 34" fill="none" stroke="#fff" stroke-width="1.6"><path d="M12 8h10l-3 5h-4z"/><path d="M15 13c-6 3-9 8-8 13 1 4 19 4 20 0 1-5-2-10-8-13"/><path d="M17 17v9M14 19h5a2 2 0 0 1 0 4h-4"/></svg></div>
    <h3>Wealth Management</h3>
    <p>Aui in eavouate velit esse ruam nihil molestiae conseruatur vera illum aui dolorem</p>
    <svg class="go" width="18" height="16" viewBox="0 0 18 16" fill="none" stroke="#2b7f78" stroke-width="2.4"><path d="M1 8h15M10 2l6 6-6 6"/></svg>
  </article>
  <article class="card" style="left:445px">
    <div class="photo" style="background:linear-gradient(135deg,#5a4a3e,#a89a8b 55%,#ddd6cc)" role="img" aria-label="Photo of two colleagues working at a laptop"></div>
    <div class="icon"><svg width="34" height="34" viewBox="0 0 34 34" fill="none" stroke="#fff" stroke-width="1.6"><rect x="4" y="4" width="26" height="26"/><path d="M9 26V18M15 26V14M21 26V20M27 26V10M8 14l7-5 6 5 7-6"/></svg></div>
    <h3>Audit Marketing</h3>
    <p>Repudiandae sint et molestiae non recusandae itaque earum aerum rioc aeneur</p>
    <svg class="go" width="18" height="16" viewBox="0 0 18 16" fill="none" stroke="#2b7f78" stroke-width="2.4"><path d="M1 8h15M10 2l6 6-6 6"/></svg>
  </article>
  <article class="card" style="left:779px">
    <div class="photo" style="background:linear-gradient(135deg,#6b3a2e,#8a8a8d 50%,#e1e4e8)" role="img" aria-label="Photo of hands reviewing financial reports beside a laptop"></div>
    <div class="icon"><svg width="34" height="34" viewBox="0 0 34 34" fill="none" stroke="#fff" stroke-width="1.6"><circle cx="17" cy="10" r="7"/><path d="M17 6v8M15 8h3a1.5 1.5 0 0 1 0 3h-3"/><path d="M17 17v13M17 24c-4 0-7-2-8-5 4 0 7 2 8 5zM17 24c4 0 7-2 8-5-4 0-7 2-8 5z"/></svg></div>
    <h3>Finance Consulting</h3>
    <p>Eius modi tempora incidunt labore et dolore magnam aliuam aerat volutatem aeneur.</p>
    <svg class="go" width="18" height="16" viewBox="0 0 18 16" fill="none" stroke="#2b7f78" stroke-width="2.4"><path d="M1 8h15M10 2l6 6-6 6"/></svg>
  </article>
</section>

<section class="mission">
  <div class="photo" role="img" aria-label="Photo of three colleagues smiling over charts at a table"></div>
  <svg class="abs" style="left:1025px;top:87px" width="175" height="395" viewBox="0 0 175 395"><polygon points="175,0 175,395 0,105" fill="#2b7f78"/></svg>
  <div class="copy">
    <div class="eyebrow" style="color:#5fb3ab;margin-top:22px;position:absolute">Who we are</div>
    <h2>Our<br>Mission,<br>Values<br>and<br>Motto</h2>
    <p>Quis autem vel eum iure reprehenderit aui in eavouate velit esse quam nihil molestiae consequatur ver illum aui dolore omnis dolor repellendus temporibus autem quibusdam et aut officiis fugiat.</p>
    <p>Illum aui dolore omnis dolor repellendus temporibus autem ruibusdam et aut officiis fugiat.</p>
    <div class="sig">Marcus Trevell</div>
  </div>
</section>
<div class="counter" style="left:112px">
  <svg width="52" height="42" viewBox="0 0 52 42" fill="none" stroke="#fff" stroke-width="1.8"><rect x="2" y="10" width="48" height="30" rx="2"/><path d="M18 10V3h16v7M2 22h48M22 22v5h8v-5"/></svg>
  <b>1,500+</b><span>Projects</span>
</div>
<div class="counter" style="left:362px">
  <svg width="42" height="46" viewBox="0 0 42 46" fill="none" stroke="#fff" stroke-width="1.8"><circle cx="21" cy="13" r="9"/><path d="M12 9h18M3 45c0-10 8-16 18-16s18 6 18 16M17 29l4 8 4-8"/></svg>
  <b>4,800+</b><span>Active clients</span>
</div>
<div class="counter" style="left:612px">
  <svg width="46" height="46" viewBox="0 0 46 46" fill="none" stroke="#fff" stroke-width="1.8"><circle cx="23" cy="20" r="11"/><path d="M18 31v6h10v-6M19 41h8M23 2v4M5 20h4M37 20h4M10 7l3 3M36 7l-3 3M23 14v12M20 17h5a2 2 0 0 1 0 4h-4"/></svg>
  <b>620+</b><span>Business Ideas</span>
</div>
<div class="counter" style="left:863px">
  <svg width="50" height="44" viewBox="0 0 50 44" fill="none" stroke="#fff" stroke-width="1.8"><path d="M2 42h46M6 42V16h12v26M18 42V4h16v38M34 42V14h12v28M22 10h3M28 10h3M22 17h3M28 17h3M22 24h3M28 24h3M10 22h4M10 30h4M38 22h4M38 30h4"/></svg>
  <b>500+</b><span>Office Branches</span>
</div>

<section class="cases">
  <div class="eyebrow abs" style="left:0;width:1200px;text-align:center;top:3255px">Recently completed</div>
  <h2 class="h2 abs" style="left:0;width:1200px;text-align:center;top:3285px;font-size:40px">Our Latest Case Studies</h2>
  <svg class="abs" style="left:190px;top:3316px" width="90" height="66" viewBox="0 0 90 66">
    <polygon points="60,50 90,66 30,66" fill="#0f1f4b"/>
    <rect x="15" y="11" width="26" height="26" transform="rotate(45 28 24)" fill="#2b7f78"/>
  </svg>

  <article class="case" style="left:112px;top:3381px">
    <div class="photo" style="background:linear-gradient(135deg,#6a6f78,#a8adb5 50%,#d9dbde)" role="img" aria-label="Photo of a calculator, laptop and printed report"></div>
    <div class="shade"></div>
    <small>Business, Finance</small><h3>Financial Report 2019</h3>
    <span class="go"><svg width="18" height="16" viewBox="0 0 18 16" fill="none" stroke="#fff" stroke-width="2.4"><path d="M1 8h15M10 2l6 6-6 6"/></svg></span>
  </article>
  <article class="case" style="left:612px;top:3381px">
    <div class="photo" style="background:linear-gradient(135deg,#c9ccd1,#9ea4ad 55%,#6f7682)" role="img" aria-label="Photo of hands passing a set of keys across a desk"></div>
    <div class="shade"></div>
    <small>Business, Finance</small><h3>MO Insurance Finance</h3>
    <span class="go"><svg width="18" height="16" viewBox="0 0 18 16" fill="none" stroke="#fff" stroke-width="2.4"><path d="M1 8h15M10 2l6 6-6 6"/></svg></span>
  </article>
  <article class="case" style="left:112px;top:3783px">
    <div class="photo" style="background:linear-gradient(135deg,#e1e3e6,#b9bdc4 55%,#858b96)" role="img" aria-label="Photo of a hand signing a loan document"></div>
    <div class="shade"></div>
    <small>Business, Finance</small><h3>Enterprise Loan 2016</h3>
    <span class="go"><svg width="18" height="16" viewBox="0 0 18 16" fill="none" stroke="#fff" stroke-width="2.4"><path d="M1 8h15M10 2l6 6-6 6"/></svg></span>
  </article>
  <article class="case" style="left:612px;top:3783px">
    <div class="photo" style="background:linear-gradient(135deg,#4b4c52,#9a9ca2 50%,#d6d8dc)" role="img" aria-label="Photo of a person with a coffee cup reviewing paperwork at a laptop"></div>
    <div class="shade"></div>
    <small>Business, Finance</small><h3>Business Growth Solutions</h3>
    <span class="go"><svg width="18" height="16" viewBox="0 0 18 16" fill="none" stroke="#fff" stroke-width="2.4"><path d="M1 8h15M10 2l6 6-6 6"/></svg></span>
  </article>
</section>

<footer class="footer">
  <div class="panel">
    <div class="brand" style="margin-bottom:44px"><span class="brand-dot"></span><span class="brand-name">PELLORY</span></div>
    <div class="contact"><svg width="13" height="13" viewBox="0 0 24 24" fill="#fff"><path d="M5 3h4l2 5-3 2a11 11 0 0 0 6 6l2-3 5 2v4a2 2 0 0 1-2 2A17 17 0 0 1 3 5a2 2 0 0 1 2-2z"/></svg>+44 20 7946 0183</div>
    <div class="contact"><svg width="13" height="11" viewBox="0 0 24 18" fill="#fff"><path d="M0 0h24v18H0z"/><path d="M0 0l12 10L24 0" stroke="#2b7f78" stroke-width="2" fill="none"/></svg>hello@pellorywealth-example.com</div>
    <div class="contact"><svg width="13" height="16" viewBox="0 0 20 26" fill="#fff"><path d="M10 0a9 9 0 0 1 9 9c0 7-9 17-9 17S1 16 1 9a9 9 0 0 1 9-9z"/><circle cx="10" cy="9" r="3" fill="#2b7f78"/></svg><span>14 Harlow Row, Bristol,<br>BS1 4QX, UK</span></div>
  </div>
  <div class="col" style="left:428px"><h4>Useful Links</h4><ul><li>Home</li><li>About us</li><li>Services</li><li>Cases</li><li>Blog</li><li>Contact us</li></ul></div>
  <div class="col" style="left:598px"><h4>Resources</h4><ul><li>Audit &amp; Assurance</li><li>Bonds &amp; Commodities</li><li>Financial Consulting</li><li>Trades &amp; Stocks</li><li>Financial Projections</li><li>Strategic Planning</li></ul></div>
  <div class="col" style="left:864px"><h4>Our Newsletter</h4>
    <div class="email">Your Email<i><svg width="16" height="16" viewBox="0 0 24 24" fill="#fff"><path d="M2 11 22 2l-9 20-2-9z"/></svg></i></div>
    <div style="font-size:13px;margin-top:16px">Follow us on:</div>
    <div class="social"><span></span><span></span><span></span></div>
  </div>
  <div class="copyright">Copyright 2022 · All Rights Reserved.</div>
</footer>

</body>
</html>
```